Velorix Flyer

PROJECT: Digital Flyer for VeloRix

Format
1920 × 1080 px (landscape, optimized for presentations and email)
Deliverables
• PDF
• PNG

About VeloRix
VeloRix is a Dutch B2B software company providing a unified CRM and customer journey platform. We help businesses manage the entire customer lifecycle — from first contact to loyal customer — by centralizing all touchpoints in one system.
What sets us apart:
Extreme ease of use. The system is self-guiding, shows only what's relevant per employee, and requires virtually no training. All channels (email, phone, chat, in-store) come together in one place with automatic task distribution. Built-in AI functions as a smart digital colleague that continuously learns.
Target audience:
Directors and sales managers at B2B companies with multiple customer contact channels.

Goal:
We want to create a flyer that sets us apart from other CRM platform providers. Our aim is to achieve this through simplicity and a professional appearance. The design should reflect our core value: ease of use. The recipient should feel compelled to engage with us — not overwhelmed by information, but intrigued by clarity. Less is more.

Required Text Elements
Headline:
"CRM that adapts to how you work"
Subline:
"Discover how VeloRix simplifies your sales process"
Call-to-action:
"See it in action — book a call"
Contact details:
• hello@velorix.nl
• 023-5718469
• velorix.com

Required Visual Elements
• VeloRix logo (attached)

Design Style
• Modern / Minimalist
• Professional / Business
• Tech / Futuristic
• Clean with plenty of whitespace

Tone of voice:
Clear, positive and customer-focused. Practical and accessible business style aimed at communicating concrete value for users.

Design inspiration — please review these websites:
• orbantal.com
• ravelo.app
• quendo.com
• tirameld.com
• gonwisp.com
What We DON'T Want
• Bold / In-your-face
• Dense / Compact
• Trendy / Experimental
• Childlike / Cheerful
• Playful / Cartoonish
• Busy / Chaotic
Colors
Use the color palette from velorix.com (blues, whites, clean professional tones).
[Exact hex codes used for element on the website:
#344054;
#1a1b1f;
#0254ac
#002249;
#e5edf7;
background-color: #fff; ]
Competitors (for context only — do NOT copy)
• brinvolt.nl
• kelmarin.com
• dortavecrm.com
• wexalunda.com
Budget
$150
Deadline
January 26, 2026

```html
<!DOCTYPE html>
<html lang="en">
<head>
<meta charset="utf-8">
<title>Velorix Flyer – 1920 × 1080 px</title>
<link rel="stylesheet" href="https://fonts.googleapis.com/css2?family=Manrope:wght@400;500;600;700&display=swap">
<style>
  :root {
    --board: #bbbbbb;
    --paper: #ffffff;
    --navy: #12224f;
    --blue: #189fdb;
    --ink: #1a1b1f;
    --faint: #f3f3f3;
    --label: #ffffff;
  }
  * { box-sizing: border-box; margin: 0; padding: 0; }
  html, body {
    width: 706px; height: 1200px; overflow: hidden;
    background: var(--board);
    font-family: "Manrope", Arial, sans-serif;
  }
  .board { position: relative; width: 706px; height: 1200px; }

  .board-title {
    position: absolute; top: 38px; left: 0; width: 706px;
    text-align: center; color: var(--label);
    font-size: 19px; font-weight: 500; letter-spacing: -0.2px;
  }
  .sample-label {
    position: absolute; left: 60px;
    transform: translate(-50%, -50%) rotate(-90deg);
    color: var(--label); font-size: 17px; font-weight: 400; white-space: nowrap;
  }

  .flyer {
    position: absolute; left: 90px; width: 549px; height: 309px;
    background: var(--paper); overflow: hidden;
    box-shadow: 8px 10px 14px rgba(0,0,0,0.18);
  }
  .flyer--one { top: 102px; }
  .flyer--two { top: 458px; }
  .flyer--three { top: 821px; }

  .backdrop-texture {
    position: absolute; left: 290px; top: 0; width: 259px; height: 309px;
    background: linear-gradient(90deg, rgba(243,243,243,0) 0%, var(--faint) 55%, var(--faint) 100%);
  }

  .headline {
    position: absolute; left: 72px; top: 40px;
    font-size: 33px; font-weight: 600; line-height: 33px; letter-spacing: -0.3px;
    color: var(--blue);
  }
  .flyer--two .headline { color: var(--navy); top: 36px; }

  .subline {
    position: absolute; left: 73px; top: 154px;
    font-size: 9.6px; line-height: 11.6px; font-weight: 500; color: var(--ink);
  }
  .flyer--two .subline {
    top: 148px; font-size: 11.4px; line-height: 13.6px; color: var(--blue);
  }

  .cta-lead {
    position: absolute; left: 80px; top: 200px;
    font-size: 7.6px; font-weight: 500; color: var(--ink);
  }
  .flyer--two .cta-lead { top: 206px; }

  .cta-button {
    position: absolute; left: 72px; top: 213px; width: 78px; height: 23px;
    border-radius: 12px; background: var(--paper);
    box-shadow: 0 1px 3px rgba(0,0,0,0.22);
    display: flex; align-items: center; justify-content: center;
    font-size: 10.4px; font-weight: 500; color: var(--ink);
  }
  .flyer--two .cta-button {
    top: 218px; background: var(--blue); color: var(--paper); box-shadow: none;
  }

  .contact {
    position: absolute; left: 73px; top: 260px;
    display: flex; align-items: center;
    font-size: 7.8px; font-weight: 500; color: var(--ink);
  }
  .flyer--two .contact { top: 269px; }
  .contact .sep { color: var(--blue); margin: 0 8px; }

  .brand {
    position: absolute; display: flex; align-items: center; gap: 8px;
    color: var(--navy); font-weight: 700;
  }
  .brand-dot { border-radius: 50%; background: var(--blue); flex: none; }
  .flyer--one .brand, .flyer--two .brand {
    left: 318px; top: 61px; width: 170px; height: 172px;
    justify-content: center; font-size: 32px;
  }
  .flyer--one .brand-dot, .flyer--two .brand-dot { width: 30px; height: 30px; }

  .flyer--three { text-align: center; }
  .flyer--three .brand {
    left: 0; width: 549px; top: 36px; height: 44px; justify-content: center; font-size: 20px; gap: 6px;
  }
  .flyer--three .brand-dot { width: 16px; height: 16px; }
  .flyer--three .headline {
    left: 0; width: 549px; top: 96px; font-size: 34px; line-height: 35px;
  }
  .flyer--three .subline {
    left: 0; width: 549px; top: 176px; font-size: 13px; line-height: 15px;
  }
  .cta-pill {
    position: absolute; left: 204px; top: 213px; width: 147px; height: 23px;
    border-radius: 12px; background: var(--paper);
    box-shadow: 0 1px 3px rgba(0,0,0,0.22);
    display: flex; align-items: center; justify-content: center; gap: 6px;
    color: var(--ink); font-weight: 500;
  }
  .cta-pill .cta-pill-lead { font-size: 7.8px; }
  .cta-pill .cta-pill-action { font-size: 10.4px; }
  .flyer--three .contact {
    left: 0; width: 549px; top: 259px; justify-content: center; font-size: 9.6px;
  }
  .flyer--three .contact .sep { margin: 0 10px; }
</style>
</head>
<body>
<main class="board">
  <h1 class="board-title">Velorix Flyer _ 1920 × 1080 px</h1>

  <span class="sample-label" style="top:256px">Sample 1</span>
  <span class="sample-label" style="top:627px">Sample 2</span>
  <span class="sample-label" style="top:990px">Sample 3</span>

  <section class="flyer flyer--one">
    <h2 class="headline">CRM that<br>adapts to how<br>you work</h2>
    <p class="subline">Discover how VeloRix simplifies<br>your sales process</p>
    <p class="cta-lead">See it in action</p>
    <div class="cta-button">BOOK A CALL</div>
    <p class="contact"><span>023-5718469</span><span class="sep">I</span><span>hello@velorix.nl</span><span class="sep">I</span><span>velorix.com</span></p>
    <div class="brand"><span class="brand-dot"></span><span>Velorix</span></div>
  </section>

  <section class="flyer flyer--two">
    <div class="backdrop-texture" role="img" aria-label="Faint light-grey background pattern of scattered brand marks"></div>
    <h2 class="headline">CRM that<br>adapts to how<br>you work</h2>
    <p class="subline">Discover how VeloRix simplifies<br>your sales process</p>
    <p class="cta-lead">See it in action</p>
    <div class="cta-button">BOOK A CALL</div>
    <p class="contact"><span>023-5718469</span><span class="sep">I</span><span>hello@velorix.nl</span><span class="sep">I</span><span>velorix.com</span></p>
    <div class="brand"><span class="brand-dot"></span><span>Velorix</span></div>
  </section>

  <section class="flyer flyer--three">
    <div class="brand"><span class="brand-dot"></span><span>Velorix</span></div>
    <h2 class="headline">CRM that adapts to<br>how you work</h2>
    <p class="subline">Discover how VeloRix simplifies your sales process</p>
    <div class="cta-pill"><span class="cta-pill-lead">See it in action</span><span class="cta-pill-action">BOOK A CALL</span></div>
    <p class="contact"><span>023-5718469</span><span class="sep">I</span><span>hello@velorix.nl</span><span class="sep">I</span><span>velorix.com</span></p>
  </section>
</main>
</body>
</html>
```